Specialist Doctor Personal Website

I wanted a website:
1. In my name
2. Describing my scope of practice
3. Having my photo
4. Has links to the places I work at
5. Provides patient information
6. Provides an email for contact

Target Market(s)

Victorian patients and GPs

Industry/Entity Type

Health

Coding

Coded - Design and coding required

Number of Pages Required

1 page

Font styles to use
Script

Colors
0054AA
0677BA
7BADD7
CADEEF
E8F1F8
6B429C
8869AF
B7A5CE
E3DAEB
F3F0F8

Requirements
Must have
• Modern design
Nice to have
• Links to email/fax/linkedin

```html
<!DOCTYPE html>
<html lang="en">
<head>
<meta charset="utf-8">
<title>Dr Rowan – Specialist Doctor</title>
<link href="https://fonts.googleapis.com/css2?family=Libre+Baskerville:wght@700&family=Poppins:wght@400;500;600&display=swap" rel="stylesheet">
<style>
:root{
  --blue-deep:#0054AA;
  --blue:#0677BA;
  --blue-soft:#7BADD7;
  --blue-pale:#CADEEF;
  --blue-mist:#E8F1F8;
  --purple:#6B429C;
  --purple-mid:#8869AF;
  --purple-soft:#B7A5CE;
  --purple-pale:#E3DAEB;
  --purple-mist:#F3F0F8;
  --ink:#222;
  --white:#fff;
  --serif:'Libre Baskerville', Georgia, serif;
  --sans:'Poppins', Arial, sans-serif;
}
*{box-sizing:border-box;margin:0;padding:0}
html,body{width:1200px;height:2818px;overflow:hidden;background:#fff}
body{font-family:var(--sans);color:var(--ink);position:relative}
.abs{position:absolute}
a{color:inherit}

/* hero */
.hero-bg{left:0;top:0;width:1200px;height:600px;background:linear-gradient(180deg,#f7f7fa 0%,#eceaf1 55%,#ece9f2 100%)}
.brand{left:104px;top:38px;display:flex;align-items:center;gap:10px;font-family:var(--sans);font-weight:600;font-size:24px;color:var(--purple)}
.brand .dot{width:26px;height:26px;border-radius:50%;border:3px solid var(--blue)}
.btn{display:flex;align-items:center;justify-content:center;font-family:var(--serif);font-size:13px;color:#fff;text-decoration:none;letter-spacing:.2px}
.login{left:977px;top:27px;width:82px;height:36px;background:var(--purple)}
.burger{left:1076px;top:36px;width:22px;height:18px;display:flex;flex-direction:column;justify-content:space-between}
.burger span{height:3px;background:#111;border-radius:2px}
.hero-title{left:103px;top:168px;font-family:var(--serif);font-size:40px;line-height:48px;color:var(--purple)}
.hero-title .accent{color:var(--blue)}
.hero-text{left:103px;top:270px;width:420px;font-size:15px;line-height:26.5px;color:#222}
.contact-item{display:flex;align-items:center;gap:12px;font-size:15px;color:var(--blue);white-space:nowrap}
.ic{width:37px;height:37px;border-radius:50%;border:2px solid var(--purple);display:flex;align-items:center;justify-content:center;flex:none}
.ic.fill{background:var(--purple)}
.book{left:104px;top:481px;width:171px;height:35px;background:var(--purple)}
.hero-frame{left:711px;top:137px;width:363px;height:560px;border:4px solid var(--purple);border-bottom-color:var(--blue);border-left:none;border-radius:0 0 180px 180px;z-index:2}
.hero-photo{left:679px;top:145px;width:388px;height:557px;border-radius:0 0 200px 200px;background:linear-gradient(180deg,#e4e4e6 0%,#d8d8dc 35%,#2d4f8f 62%,#1d3a78 100%);z-index:3}

/* scope */
.scope-bg{left:0;top:600px;width:1200px;height:675px;background:linear-gradient(180deg,#ece9f2 0%,#f4f3f7 100%)}
.section-title{font-family:var(--serif);font-size:30px;color:var(--purple);text-align:center;width:1200px;left:0}
.card{top:868px;width:227px;height:268px;border-radius:4px;color:#fff;text-align:center;padding:62px 8px 0}
.card h3{font-family:var(--serif);font-size:19px;font-weight:700;margin-bottom:12px}
.card p{font-size:13px;line-height:23.2px;opacity:.92}
.card .more{display:block;margin-top:8px;font-family:var(--serif);font-size:16px;font-weight:700;text-decoration:underline}
.card .badge{position:absolute;left:66px;top:-47px;width:95px;height:95px;border-radius:50%;border:3px solid #fff;display:flex;align-items:center;justify-content:center}
.c1{left:103px;background:var(--blue)}
.c1 .badge{background:var(--blue)}
.c2{left:359px;background:linear-gradient(180deg,var(--blue) 0%,var(--purple) 100%);box-shadow:0 14px 28px rgba(60,40,110,.35)}
.c2 .badge{background:linear-gradient(180deg,var(--blue),var(--purple))}
.c3{left:614px;background:var(--purple-soft)}
.c3 .badge{background:var(--purple-soft)}
.c4{left:869px;background:var(--blue-soft)}
.c4 .badge{background:var(--blue-soft)}

/* places */
.map{left:213px;top:1365px;width:385px;height:355px;border-radius:40% 48% 42% 38%;background:radial-gradient(circle at 50% 40%,var(--blue) 0%,var(--purple-mid) 60%,var(--purple) 100%);opacity:.85}
.places-title{left:700px;top:1428px;font-family:var(--serif);font-size:30px;color:var(--purple)}
.places-list{left:700px;top:1478px;list-style:none}
.places-list li{display:flex;align-items:center;gap:6px;height:29.8px;font-size:16px;color:var(--blue)}

/* patient */
.patient-bg{left:0;top:1800px;width:1200px;height:399px;background:#f3f3f5}
.patient-text{left:0;top:1918px;width:1200px;text-align:center;font-size:16.5px;line-height:27px;color:#333}
.patient-text p+p{margin-top:10px}
.patient-btn{left:545px;top:2082px;width:110px;height:36px;background:var(--purple)}

/* contact */
.contact-bg{left:0;top:2199px;width:1200px;height:539px;background:linear-gradient(180deg,var(--blue) 0%,#3c5fb0 55%,var(--purple) 100%)}
.field{border:1px solid rgba(255,255,255,.75);color:#fff;font-size:13px;font-weight:500;padding:0 14px;display:flex;align-items:center}
.field.area{align-items:flex-start;padding-top:16px}
.submit{left:174px;top:2648px;width:113px;height:39px;border:1px solid #fff;border-radius:3px;color:#fff;font-size:14px;font-weight:600;display:flex;align-items:center;justify-content:center}
.info-ic{width:48px;height:48px;border-radius:50%;border:2px solid rgba(255,255,255,.8);display:flex;align-items:center;justify-content:center}
.info h4{font-size:20px;font-weight:600;color:#fff;letter-spacing:.5px}
.info p{font-size:15px;line-height:22px;color:#fff;white-space:nowrap}
.contact-photo{left:977px;top:2374px;width:223px;height:364px;border-radius:110px 110px 0 0;background:linear-gradient(180deg,#c9b9a8 0%,#8b6f5c 30%,#1f3d3f 60%,#152c30 100%)}

/* footer */
.copy{left:104px;top:2771px;font-size:12px;color:#222}
.foot-ic{top:2762px;width:34px;height:34px;border-radius:50%;background:var(--purple);display:flex;align-items:center;justify-content:center}
</style>
</head>
<body>

<!-- Hero -->
<div class="abs hero-bg" role="img" aria-label="Soft faded city skyline backdrop"></div>
<div class="abs brand"><span class="dot"></span>Rowan</div>
<a class="abs btn login" href="#">LOG IN</a>
<div class="abs burger"><span></span><span></span><span></span></div>

<h1 class="abs hero-title">Specialist Doctor<br><span class="accent">Hi I'm Rowan</span></h1>
<p class="abs hero-text">Lorem ipsum dolor sit amet, consectetur adipiscing elit, sed do eiusmod tempor incididunt ut labore et dolore magna aliqua.</p>

<div class="abs contact-item" style="left:105px;top:370px">
  <span class="ic fill"><svg width="16" height="12" viewBox="0 0 16 12"><rect x="0" y="0" width="16" height="12" rx="1.5" fill="#fff"/><path d="M1 1l7 6 7-6" stroke="var(--purple)" stroke-width="1.6" fill="none"/></svg></span>
  <a href="#">info@rowan.example</a>
</div>
<div class="abs contact-item" style="left:319px;top:370px">
  <span class="ic"><svg width="14" height="14" viewBox="0 0 24 24"><path d="M6.6 10.8a15 15 0 006.6 6.6l2.2-2.2a1 1 0 011-.25 11.4 11.4 0 003.6.57 1 1 0 011 1V20a1 1 0 01-1 1A17 17 0 013 4a1 1 0 011-1h3.5a1 1 0 011 1 11.4 11.4 0 00.57 3.6 1 1 0 01-.25 1z" fill="var(--purple)"/></svg></span>
  <span>+61 3 9000 4410</span>
</div>
<div class="abs contact-item" style="left:105px;top:425px">
  <span class="ic"><svg width="12" height="16" viewBox="0 0 12 16"><path d="M6 0a6 6 0 00-6 6c0 4.5 6 10 6 10s6-5.5 6-10a6 6 0 00-6-6z" fill="var(--purple)"/><circle cx="6" cy="6" r="2.2" fill="#fff"/></svg></span>
  <span>View Locations</span>
</div>
<div class="abs contact-item" style="left:319px;top:425px">
  <span class="ic"><svg width="16" height="14" viewBox="0 0 16 14"><rect x="3" y="0" width="10" height="5" fill="none" stroke="var(--purple)" stroke-width="1.5"/><rect x="0" y="4" width="16" height="10" rx="1.5" fill="var(--purple)"/><rect x="4" y="8" width="8" height="2" fill="#fff"/></svg></span>
  <span>9000 4411</span>
</div>
<div class="abs" style="left:487px;top:425px">
  <span class="ic"><svg width="16" height="16" viewBox="0 0 16 16" fill="none" stroke="var(--purple)" stroke-width="1.8" stroke-linecap="round"><path d="M7 9a3 3 0 004 0l3-3a3 3 0 00-4-4l-1 1"/><path d="M9 7a3 3 0 00-4 0l-3 3a3 3 0 004 4l1-1"/></svg></span>
</div>
<a class="abs btn book" href="#">BOOK APPOINTMENT</a>

<!-- Scope of practice -->
<div class="abs scope-bg" role="img" aria-label="Subtle light lattice pattern background"></div>

<div class="abs hero-frame"></div>
<div class="abs hero-photo" role="img" aria-label="Portrait photo of the doctor in a navy suit"></div>

<h2 class="abs section-title" style="top:756px">MY SCOPE OF PRACTICE</h2>

<div class="abs card c1">
  <div class="badge"><svg width="48" height="48" viewBox="0 0 48 48" fill="none" stroke="#fff" stroke-width="2.2" stroke-linecap="round"><path d="M12 6v12a8 8 0 0016 0V6"/><path d="M20 26v6a8 8 0 0016 0v-4"/><circle cx="36" cy="24" r="4"/></svg></div>
  <h3>Lorem ipsum dolor</h3>
  <p>Lorem ipsum dolor sit amet, consectetur adipiscing elit, sed do eiusmod tempor incididunt ut labore et dolore magna aliqua.</p>
  <a class="more" href="#">Read More</a>
</div>
<div class="abs card c2">
  <div class="badge"><svg width="50" height="48" viewBox="0 0 50 48" fill="none" stroke="#fff" stroke-width="2.2" stroke-linejoin="round"><circle cx="25" cy="14" r="10"/><path d="M25 9v10M20 14h10"/><path d="M6 30h38v10H6z"/><path d="M6 30v-6M44 30v-6"/></svg></div>
  <h3>Lorem ipsum dolor</h3>
  <p>Lorem ipsum dolor sit amet, consectetur adipiscing elit, sed do eiusmod tempor incididunt ut labore et dolore magna aliqua.</p>
  <a class="more" href="#">Read More</a>
</div>
<div class="abs card c3">
  <div class="badge"><svg width="44" height="50" viewBox="0 0 44 50" fill="none" stroke="#333" stroke-width="2" stroke-linejoin="round"><path d="M8 4h22l8 8v34H8z"/><path d="M19 12v10M14 17h10"/><path d="M14 28h18M14 34h18M14 40h12"/></svg></div>
  <h3>Lorem ipsum dolor</h3>
  <p>Lorem ipsum dolor sit amet, consectetur adipiscing elit, sed do eiusmod tempor incididunt ut labore et dolore magna aliqua.</p>
  <a class="more" href="#">Read More</a>
</div>
<div class="abs card c4">
  <div class="badge"><svg width="50" height="48" viewBox="0 0 50 48" fill="none" stroke="#333" stroke-width="2" stroke-linejoin="round"><rect x="4" y="8" width="42" height="28" rx="2"/><path d="M18 44h14M25 36v8"/><circle cx="25" cy="18" r="5"/><path d="M16 34a9 9 0 0118 0"/></svg></div>
  <h3>Lorem ipsum dolor</h3>
  <p>Lorem ipsum dolor sit amet, consectetur adipiscing elit, sed do eiusmod tempor incididunt ut labore et dolore magna aliqua.</p>
  <a class="more" href="#">Read More</a>
</div>

<!-- Places -->
<div class="abs map" role="img" aria-label="Dotted map of Australia in blue and purple"></div>
<h2 class="abs places-title">PLACES I WORK AT</h2>
<ul class="abs places-list">
  <li><svg width="10" height="14" viewBox="0 0 12 16"><path d="M6 0a6 6 0 00-6 6c0 4.5 6 10 6 10s6-5.5 6-10a6 6 0 00-6-6z" fill="var(--blue)"/><circle cx="6" cy="6" r="2.2" fill="#fff"/></svg>Lorem ipsum dolor sit</li>
  <li><svg width="10" height="14" viewBox="0 0 12 16"><path d="M6 0a6 6 0 00-6 6c0 4.5 6 10 6 10s6-5.5 6-10a6 6 0 00-6-6z" fill="var(--blue)"/><circle cx="6" cy="6" r="2.2" fill="#fff"/></svg>Lorem ipsum dolor sit</li>
  <li><svg width="10" height="14" viewBox="0 0 12 16"><path d="M6 0a6 6 0 00-6 6c0 4.5 6 10 6 10s6-5.5 6-10a6 6 0 00-6-6z" fill="var(--blue)"/><circle cx="6" cy="6" r="2.2" fill="#fff"/></svg>Lorem ipsum dolor sit</li>
  <li><svg width="10" height="14" viewBox="0 0 12 16"><path d="M6 0a6 6 0 00-6 6c0 4.5 6 10 6 10s6-5.5 6-10a6 6 0 00-6-6z" fill="var(--blue)"/><circle cx="6" cy="6" r="2.2" fill="#fff"/></svg>Lorem ipsum dolor sit</li>
  <li><svg width="10" height="14" viewBox="0 0 12 16"><path d="M6 0a6 6 0 00-6 6c0 4.5 6 10 6 10s6-5.5 6-10a6 6 0 00-6-6z" fill="var(--blue)"/><circle cx="6" cy="6" r="2.2" fill="#fff"/></svg>Lorem ipsum dolor sit</li>
  <li><svg width="10" height="14" viewBox="0 0 12 16"><path d="M6 0a6 6 0 00-6 6c0 4.5 6 10 6 10s6-5.5 6-10a6 6 0 00-6-6z" fill="var(--blue)"/><circle cx="6" cy="6" r="2.2" fill="#fff"/></svg>Lorem ipsum dolor sit</li>
</ul>

<!-- Patient information -->
<div class="abs patient-bg"></div>
<h2 class="abs section-title" style="top:1865px">PATIENT INFORMATION</h2>
<div class="abs patient-text">
  <p>Lorem ipsum dolor sit amet, consectetur adipiscing elit, sed do eiusmod tempor incididunt ut labore et dolore magna aliqua.<br>Quis ipsum suspendisse ultrices gravida. Risus commodo viverra maecenas accumsan<br>lacus vel facilisis.</p>
  <p>Lorem ipsum dolor sit amet, consectetur adipiscing elit, sed do eiusmod tempor incididunt ut labore et dolore magna aliqua.<br>Quis ipsum suspendisse ultrices gravida.</p>
</div>
<a class="abs btn patient-btn" href="#">READ MORE</a>

<!-- Contact -->
<div class="abs contact-bg" role="img" aria-label="City skyline in blue and purple tint"></div>
<h2 class="abs section-title" style="top:2285px;color:#fff">CANTACT US</h2>

<div class="abs field" style="left:174px;top:2377px;width:451px;height:47px">Name</div>
<div class="abs field" style="left:174px;top:2437px;width:221px;height:47px">Email</div>
<div class="abs field" style="left:405px;top:2437px;width:220px;height:47px">Phone</div>
<div class="abs field area" style="left:174px;top:2498px;width:451px;height:131px">Message</div>
<div class="abs submit">SUBMIT</div>

<div class="abs info-ic" style="left:682px;top:2371px"><svg width="14" height="19" viewBox="0 0 12 16"><path d="M6 0a6 6 0 00-6 6c0 4.5 6 10 6 10s6-5.5 6-10a6 6 0 00-6-6z" fill="#fff"/><circle cx="6" cy="6" r="2.2" fill="var(--blue)"/></svg></div>
<div class="abs info" style="left:749px;top:2366px">
  <h4>Location :</h4>
  <p>200 Harbour Lane Lorem<br>ipsum dolor sit &nbsp;3000</p>
</div>
<div class="abs info-ic" style="left:682px;top:2472px"><svg width="18" height="18" viewBox="0 0 24 24"><path d="M6.6 10.8a15 15 0 006.6 6.6l2.2-2.2a1 1 0 011-.25 11.4 11.4 0 003.6.57 1 1 0 011 1V20a1 1 0 01-1 1A17 17 0 013 4a1 1 0 011-1h3.5a1 1 0 011 1 11.4 11.4 0 00.57 3.6 1 1 0 01-.25 1z" fill="#fff"/></svg></div>
<div class="abs info" style="left:749px;top:2468px">
  <h4>Phone :</h4>
  <p>+61 3 9000 4410</p>
</div>
<div class="abs info-ic" style="left:682px;top:2557px"><svg width="20" height="15" viewBox="0 0 16 12"><rect width="16" height="12" rx="1.5" fill="#fff"/><path d="M1 1l7 6 7-6" stroke="var(--purple)" stroke-width="1.6" fill="none"/></svg></div>
<div class="abs info" style="left:749px;top:2553px">
  <h4>Email :</h4>
  <p>info@rowan.example</p>
</div>
<div class="abs contact-photo" role="img" aria-label="Photo of the doctor in a dark green blazer"></div>

<!-- Footer -->
<p class="abs copy">© 2023 Rowan | All Rights Reserved</p>
<div class="abs foot-ic" style="left:975px"><svg width="15" height="11" viewBox="0 0 16 12"><rect width="16" height="12" rx="1.5" fill="#fff"/><path d="M1 1l7 6 7-6" stroke="var(--purple)" stroke-width="1.6" fill="none"/></svg></div>
<div class="abs foot-ic" style="left:1019px"><svg width="15" height="13" viewBox="0 0 16 14"><rect x="3" y="0" width="10" height="5" fill="none" stroke="#fff" stroke-width="1.5"/><rect x="0" y="4" width="16" height="10" rx="1.5" fill="#fff"/><rect x="4" y="8" width="8" height="2" fill="var(--purple)"/></svg></div>
<div class="abs foot-ic" style="left:1062px"><svg width="15" height="15" viewBox="0 0 16 16" fill="none" stroke="#fff" stroke-width="1.8" stroke-linecap="round"><path d="M7 9a3 3 0 004 0l3-3a3 3 0 00-4-4l-1 1"/><path d="M9 7a3 3 0 00-4 0l-3 3a3 3 0 004 4l1-1"/></svg></div>

</body>
</html>
```